Labels designs for a new coffee brand (Vestro Coffee)

We looking for a coffee label design for our coffee Brand, VESTRO COFFE, attached is the logo. We are bringing out to the market 3 Premium blends
1. Colombian Popayan
2. Gourmet Expresso Blend
3. Brazilian Santos

We like something that looks high quality yet modern, the bags we are using is black matte, we are starting with labels and look in the near future to print our own labels .

We want the labels for the 3 coffees to have the similar look and feel but to be uniquely identified by its design (Colombian, Brazilian, espresso) This is beig sold as a set so we want it to have a similar label feeling but that each is identify as its unique product (colombian, expresso, brazilian blend.

This project is for labels that will be used on a black matte bag, is for a 16 oz bag,

Attached is a sample of the bag color.

Size Requirements:
Maintain a 2:3 aspect ratio for the image file
The label will be 4" wide and 6" tall (we also want to print some 3X4)
Recommended image size is 1600px X 2400px

I will provide upc later

www.vestrocoffee.example pw 48071 this is the test site not live yet but you can get a feel of the brand
Updates

Ay my daughters volleyball tournament I need extra time to review

Target Market(s)

coffee drinkers

Industry/Entity Type

coffee

Requirements
Must have
• Creativity, unique, eye catchy,

```html
<!DOCTYPE html>
<html lang="en">
<head>
<meta charset="utf-8">
<title>Vestro Coffee – Brazilian Santos Label</title>
<link href="https://fonts.googleapis.com/css2?family=Bebas+Neue&family=Archivo:wght@400;600;700&display=swap" rel="stylesheet">
<style>
  :root {
    --stage: #a6a89b;
    --label-white: #fbfbf8;
    --brand-green: #17a444;
    --brand-green-light: #2fbe66;
    --ink: #1c1c1c;
    --mark-khaki: #bdb89d;
  }
  html, body { margin: 0; padding: 0; overflow: hidden; }
  body {
    width: 1200px; height: 900px;
    background: var(--stage);
    position: relative;
    font-family: "Archivo", Arial, sans-serif;
  }
  .label {
    position: absolute; left: 400px; top: 150px;
    width: 400px; height: 600px;
    background: var(--label-white);
    overflow: hidden;
    box-shadow: 0 2px 10px rgba(0,0,0,.18);
  }
  .artwork {
    position: absolute; left: 0; top: 0;
    width: 240px; height: 440px;
  }
  .brand-band {
    position: absolute; right: 0; top: 0;
    width: 112px; height: 600px;
  }
  .brand-name {
    position: absolute; right: 22px; top: 150px;
    writing-mode: vertical-rl;
    font-family: "Bebas Neue", Impact, sans-serif;
    font-size: 84px; letter-spacing: 8px; line-height: 1;
    color: var(--mark-khaki);
    margin: 0;
  }
  .brand-dot {
    position: absolute; right: 31px; top: 72px;
    width: 46px; height: 46px; border-radius: 50%;
    background: var(--mark-khaki);
  }
  .product-name {
    position: absolute; right: 120px; top: 232px;
    margin: 0; text-align: right;
    font-family: "Bebas Neue", Impact, sans-serif;
    font-size: 50px; line-height: 0.9; letter-spacing: 0.5px;
    color: var(--brand-green);
  }
  .roast-badge {
    position: absolute; left: 146px; top: 322px;
    width: 130px; height: 130px;
  }
  .roast-badge__text {
    position: absolute; inset: 0;
    display: flex; flex-direction: column; align-items: center; justify-content: center;
    color: var(--label-white); line-height: 1;
  }
  .roast-badge__pct { font-weight: 700; font-size: 24px; }
  .roast-badge__small { font-size: 13px; margin-top: 2px; }
  .roast-badge__big { font-size: 19px; }
  .cup-notes {
    position: absolute; left: 66px; top: 461px;
    width: 210px; border-collapse: collapse;
    border: 1.5px solid var(--brand-green);
  }
  .cup-notes td {
    border: 1px solid var(--brand-green);
    padding: 2px 4px; color: var(--ink);
    font-size: 10px; height: 14px; text-transform: uppercase;
  }
  .cup-notes .cup-notes__title { font-size: 17px; font-weight: 600; height: 22px; }
  .cup-notes .cup-notes__blank { width: 66px; }
  .net-weight {
    position: absolute; left: 66px; top: 560px; margin: 0;
    font-size: 10px; font-weight: 700; color: var(--brand-green);
  }
</style>
</head>
<body>
  <section class="label">
    <svg class="artwork" viewBox="0 0 240 440" role="img" aria-label="Green line-art illustration of abstract cubist faces">
      <defs>
        <linearGradient id="artTone" x1="0" y1="0" x2="1" y2="1">
          <stop offset="0" stop-color="#6fcf8f"/>
          <stop offset="1" stop-color="#d6f0dd"/>
        </linearGradient>
      </defs>
      <path d="M0 0 H240 V230 H120 V440 H0 Z" fill="url(#artTone)"/>
    </svg>

    <svg class="brand-band" viewBox="0 0 112 600" aria-hidden="true">
      <defs>
        <linearGradient id="bandTone" x1="0" y1="0" x2="0" y2="1">
          <stop offset="0" stop-color="#17a444"/>
          <stop offset="1" stop-color="#32c06a"/>
        </linearGradient>
      </defs>
      <path fill="url(#bandTone)" d="M112 0 V600 H10
        q-8 -6 0 -12 q-8 -6 0 -12 q-8 -6 0 -12 q-8 -6 0 -12 q-8 -6 0 -12
        q-8 -6 0 -12 q-8 -6 0 -12 q-8 -6 0 -12 q-8 -6 0 -12 q-8 -6 0 -12
        q-8 -6 0 -12 q-8 -6 0 -12 q-8 -6 0 -12 q-8 -6 0 -12 q-8 -6 0 -12
        q-8 -6 0 -12 q-8 -6 0 -12 q-8 -6 0 -12 q-8 -6 0 -12 q-8 -6 0 -12
        q-8 -6 0 -12 q-8 -6 0 -12 q-8 -6 0 -12 q-8 -6 0 -12 q-8 -6 0 -12
        q-8 -6 0 -12 q-8 -6 0 -12 q-8 -6 0 -12 q-8 -6 0 -12 q-8 -6 0 -12
        q-8 -6 0 -12 q-8 -6 0 -12 q-8 -6 0 -12 q-8 -6 0 -12 q-8 -6 0 -12
        q-8 -6 0 -12 q-8 -6 0 -12 q-8 -6 0 -12 q-8 -6 0 -12 q-8 -6 0 -12
        q-8 -6 0 -12 q-8 -6 0 -12 q-8 -6 0 -12 q-8 -6 0 -12 q-8 -6 0 -12
        q-8 -6 0 -12 q-8 -6 0 -12 q-8 -6 0 -12 q-8 -6 0 -12 q-8 -6 0 -12 Z"/>
    </svg>
    <span class="brand-dot" aria-hidden="true"></span>
    <p class="brand-name">VESTRO</p>

    <h1 class="product-name">Brazilian<br>Santos</h1>

    <div class="roast-badge">
      <svg viewBox="0 0 130 130" width="130" height="130" aria-hidden="true">
        <path fill="var(--brand-green)" d="M65 8 L76 28 L98 18 L96 42 L122 46 L104 64 L124 82 L98 86 L102 112 L78 100 L66 124 L54 102 L30 114 L34 90 L8 84 L26 66 L10 46 L34 42 L32 18 L54 28 Z"/>
      </svg>
      <div class="roast-badge__text">
        <span class="roast-badge__pct">100%</span>
        <span class="roast-badge__small">ROASTED</span>
        <span class="roast-badge__big">COFFEE</span>
      </div>
    </div>

    <table class="cup-notes">
      <tr><td class="cup-notes__title">Cup Notes</td><td class="cup-notes__blank" rowspan="4"></td></tr>
      <tr><td>Orange Citrus</td></tr>
      <tr><td>Dark Caramel</td></tr>
      <tr><td>Nakers Chocolate</td></tr>
    </table>

    <p class="net-weight">NET WEIGHT | 16 OZ</p>
  </section>
</body>
</html>
```